External Window Signage Design - Dentist

We have 5 windows that need to have new signage designed for a Dental Clinic based in a community shopping centre.
The windows mostly line up but there is one smaller window which is lower to the ground. All 5 windows are to be covered with vinyl graphics
The windows all face the shopping centre car park under an awning.

We have attached the measurements of the window to have graphics.
We will be placing perforated once way vision vinyl as a material on the external glass. We have also attach our logo design.

We would like something simple and creative for our design. Stock images should only be used to aid in aethetics but not form the basis of the design. We prefer simple custom graphics that identifies us as a clean, modern dental clinic. We are marketing ourselves as a modern fully digital clinic where all examinations are done on a big screen which photography and 3d scanners.

Please include the words below.

Marlow Ridge Dental

Children's Dentistry
Digital Dentistry
Cosmetic Dentistry
Clearvanta
Family Dental Care
Where quality meets value - This one is our slogan, and not a service. Please use it as such.
Same Day Emergency Bookings

Please include in small text our website and phone number.
www.marlowridgedental.com.au
Phone Number TBD: 87650432

Open to different colors but our main theme is blues and greens. Similar to our logo.

Target Market(s)

20 - 40 year old dental patients. Middle Class. Some retirees as well.

Industry/Entity Type

Dental Clinic

Font styles to use
Other font styles liked:
• Comfortaa

Colors
33b8a4
34a6d7

Requirements
Must have
• Simple elegant graphics. Stock photos to aid in design if needed.
Nice to have
• Simple designs with greys, greens and blues. As per our logo.
Comfortaa font
Should not have
• Overbearing stock imagery.
Too many colors.

```html
<!DOCTYPE html>
<html lang="en">
<head>
<meta charset="utf-8">
<title>Marlow Ridge Dental – Window Signage Options</title>
<link href="https://fonts.googleapis.com/css2?family=Comfortaa:wght@300;400;700&display=swap" rel="stylesheet">
<style>
  :root{
    --bg:#e4e8e8;
    --blue:#3fbaf9;
    --green:#7df914;
    --grey:#7c8287;
    --ink:#55595d;
    --navy:#1d3b5c;
    --white:#ffffff;
    --rule:#9aa3a8;
  }
  *{box-sizing:border-box;margin:0;padding:0}
  html,body{width:1200px;height:1200px;overflow:hidden;background:var(--bg)}
  body{position:relative;font-family:'Comfortaa',sans-serif;color:var(--ink)}
  .option-label{position:absolute;left:209px;font-size:19px;font-weight:400;font-variant:small-caps;letter-spacing:.5px;color:#555}
  .window{position:absolute;overflow:hidden;background:var(--white)}
  .window--blue{background:var(--blue)}
  .window--green{background:var(--green)}
  .divider-left{border-left:1px solid #8a9196}

  /* brand name in place of logo */
  .brand{position:absolute;display:flex;flex-direction:column;align-items:center;text-align:center}
  .brand__dot{width:44px;height:44px;border-radius:50%;border:4px solid var(--grey);margin-bottom:8px}
  .brand__name{font-size:16px;font-weight:400;color:var(--blue);white-space:nowrap;letter-spacing:.3px}
  .brand__contact{margin-top:18px;font-size:6.5px;line-height:1.35;color:var(--ink)}

  .brand-vertical{position:absolute;left:50%;top:46%;display:flex;align-items:center;gap:8px;transform:translate(-50%,-50%) rotate(-90deg);white-space:nowrap}
  .brand-vertical .brand__dot{margin:0;width:30px;height:30px;border-width:3px}
  .brand-vertical .brand__name{font-size:17px}
  .small-contact{position:absolute;left:0;right:0;bottom:26px;text-align:center;font-size:5.5px;line-height:1.35;color:var(--ink)}

  /* slogans */
  .slogan-caps{position:absolute;left:0;right:0;top:128px;text-align:center;font-weight:300;font-size:39px;line-height:41px;color:var(--white)}
  .slogan-caps .accent{color:var(--green);font-weight:400}
  .slogan-script{position:absolute;left:28px;top:40px;font-size:42px;line-height:39px;color:var(--blue);font-weight:300}
  .slogan-script .accent{color:var(--green);font-weight:700}

  /* services */
  .services{position:absolute;left:50%;transform:translateX(-50%);list-style:none;text-align:center}
  .services li{height:20.6px;line-height:19px;border-bottom:1px solid var(--rule);white-space:nowrap}
  .services li:last-child{border-bottom:none}
  .services--on-green{top:164px;width:142px;font-size:13.5px;color:var(--white)}
  .services--on-green li{border-color:#6b8f5a}
  .services--on-white{top:84px;width:142px;font-size:13.5px;color:var(--ink)}

  /* emergency band */
  .emergency{position:absolute;right:0;text-align:center;color:var(--white)}
  .emergency__top{background:var(--green);clip-path:polygon(12% 0,100% 0,100% 100%,0 100%);line-height:1.15}
  .emergency__bottom{background:var(--blue);clip-path:polygon(12% 0,100% 0,100% 100%,0 100%)}
  .emergency--sm{top:29px;width:156px}
  .emergency--sm .emergency__top{margin-left:18px;height:20px;font-size:7px;padding-top:2px;padding-left:16px}
  .emergency--sm .emergency__bottom{height:20px;font-size:10px;line-height:20px;padding-left:16px}
  .emergency--lg{top:86px;width:221px}
  .emergency--lg .emergency__top{margin-left:26px;height:27px;font-size:9.5px;padding-top:3px;padding-left:24px}
  .emergency--lg .emergency__bottom{height:27px;font-size:14px;line-height:27px;padding-left:20px}

  /* health funds */
  .funds{position:absolute;display:grid;grid-template-columns:repeat(3,50px);column-gap:3px;row-gap:14px;align-items:center}
  .funds__label{font-size:5.8px;line-height:1.3;color:var(--blue)}
  .funds__name{font-size:7px;line-height:1.1;font-weight:700;color:var(--navy)}
  .funds__name--blue{color:var(--blue)}
  .funds__name--grey{color:var(--ink)}

  .photo-fill{position:absolute;left:0;right:0;bottom:0;height:196px;background:linear-gradient(180deg,rgba(255,255,255,0) 0%,#bfe9e6 35%,#6fd3cc 100%)}
  .photo-fade{position:absolute;left:0;bottom:0;width:120px;height:196px;background:linear-gradient(90deg,#c9eeeb 0%,rgba(255,255,255,0) 100%)}
  .faint-ring{position:absolute;left:0;top:152px;width:330px;height:330px;border-radius:50%;border:14px solid #eceeef}
</style>
</head>
<body>

<h2 class="option-label" style="top:40px">Option 3</h2>

<section class="window" style="left:73px;top:145px;width:117px;height:359px">
  <div class="brand-vertical"><span class="brand__dot"></span><span class="brand__name">Marlow Ridge Dental</span></div>
  <p class="small-contact">www.marlowridgedental.com.au<br>Phone Number TBD: 87650432</p>
</section>

<section class="window window--blue" style="left:212px;top:78px;width:231px;height:427px">
  <p class="slogan-caps">WHERE<br>QUALITY<br><span class="accent">MEETS<br>VALUE</span></p>
</section>

<section class="window divider-left" style="left:444px;top:78px;width:231px;height:427px">
  <div class="brand" style="left:0;right:0;top:170px">
    <span class="brand__dot"></span>
    <span class="brand__name">Marlow Ridge Dental</span>
    <p class="brand__contact">www.marlowridgedental.com.au<br>Phone Number TBD: 87650432</p>
  </div>
</section>

<section class="window window--green divider-left" style="left:675px;top:78px;width:232px;height:427px">
  <ul class="services services--on-green">
    <li>Children's Dentistry</li><li>Digital Dentistry</li><li>Cosmetic Dentistry</li><li>Clearvanta</li><li>Family Dental Care</li>
  </ul>
</section>

<section class="window divider-left" style="left:929px;top:78px;width:196px;height:427px">
  <div class="emergency emergency--sm">
    <div class="emergency__top">Same Day<br>EMERGENCY BOOKINGS</div>
    <div class="emergency__bottom">Ph. TBD: 87650432</div>
  </div>
  <div class="brand" style="left:0;right:0;top:170px">
    <span class="brand__dot"></span>
    <span class="brand__name">Marlow Ridge Dental</span>
  </div>
  <div class="funds" style="left:25px;top:296px">
    <span class="funds__label">HEALTHFUND<br>PROVIDERS</span>
    <span class="funds__name funds__name--blue">Kestrel<br>Health</span>
    <span class="funds__name">Tutor<br>Cover</span>
    <span class="funds__name funds__name--grey">Guardline</span>
    <span class="funds__name funds__name--blue">Ovalis</span>
    <span class="funds__name">Southward<br>Mutual</span>
  </div>
</section>

<h2 class="option-label" style="top:648px">Option 4</h2>

<section class="window" style="left:75px;top:760px;width:115px;height:362px">
  <div class="brand-vertical"><span class="brand__dot"></span><span class="brand__name">Marlow Ridge Dental</span></div>
  <p class="small-contact">www.marlowridgedental.com.au<br>Phone Number TBD: 87650432</p>
</section>

<section class="window" style="left:212px;top:691px;width:232px;height:431px">
  <p class="slogan-script">Where<br>quality<br><span class="accent">meets<br>value</span></p>
  <div class="photo-fill" role="img" aria-label="Photo of a model tooth, stethoscope and dental mirror on a soft aqua surface"></div>
</section>

<section class="window divider-left" style="left:444px;top:691px;width:231px;height:431px">
  <div class="photo-fade"></div>
  <ul class="services services--on-white">
    <li>Children's Dentistry</li><li>Digital Dentistry</li><li>Cosmetic Dentistry</li><li>Clearvanta</li><li>Family Dental Care</li>
  </ul>
  <div class="brand" style="left:0;right:0;top:252px">
    <span class="brand__dot"></span>
    <span class="brand__name">Marlow Ridge Dental</span>
    <p class="brand__contact">www.marlowridgedental.com.au<br>Phone Number TBD: 87650432</p>
  </div>
</section>

<section class="window" style="left:675px;top:691px;width:232px;height:431px">
  <span style="position:absolute;left:0;top:0;height:308px;border-left:1px solid #8a9196"></span>
  <div class="emergency emergency--lg">
    <div class="emergency__top">Same Day<br>EMERGENCY BOOKINGS</div>
    <div class="emergency__bottom">Ph. TBD: 87650432</div>
  </div>
  <div class="funds" style="left:37px;top:164px">
    <span class="funds__label">HEALTHFUND<br>PROVIDERS</span>
    <span class="funds__name funds__name--blue">Kestrel<br>Health</span>
    <span class="funds__name">Tutor<br>Cover</span>
    <span class="funds__name funds__name--grey">Guardline</span>
    <span class="funds__name funds__name--blue">Ovalis</span>
    <span class="funds__name">Southward<br>Mutual</span>
  </div>
</section>

<section class="window" style="left:929px;top:691px;width:197px;height:431px">
  <div class="brand" style="left:0;right:0;top:48px">
    <span class="brand__dot"></span>
    <span class="brand__name">Marlow Ridge Dental</span>
  </div>
  <div class="faint-ring"></div>
</section>

</body>
</html>
```